Stationary Design needed for luxorious bespoke tailor

We need a design for our stationary items like businescards, letters, envelope and letter head / Signature for email. Our company "VELMARDO" sells exclusively and luxourious bespoke garments and accessories for men. The desgins of letterhead, envelope and business card shoulderstand communicate luxury, high quality and good taste. We would like our logo to be used on the designs.

Target Market(s)

Gentleman with a high aproach and exclusive and luxourious suits and shirts, grooms, businesman,

Industry/Entity Type

It Company

Font styles to use
Sans Serif

Colors
ec1f27
ffffff

Requirements
Must have
• Logo, Companies name and adress, contactName internet & email, phone number line / mobile, VAT Nr. On Business Card frontpage only logo and name, adress companies on backpage. No VAT and Companies ID there. Company data; VELMARDO AG Sonnwiesweg 27 4068 Basel Switzerland VAT: CHE 472 916 503 Tax Tel 41 61 508 37 14 Mobile 41 79 842 07 91 www.velmardo.ch info@velmardo.com.
Nice to have
• -Name And phone numbers need to be able to change (for different coworkers ...)
Should not have
• no VAT in Business Card

```html
<!DOCTYPE html>
<html lang="en">
<head>
<meta charset="utf-8">
<title>VELMARDO – Stationery</title>
<link href="https://fonts.googleapis.com/css2?family=Montserrat:wght@600&family=Roboto+Slab:wght@300;400&display=swap" rel="stylesheet">
<style>
  :root{
    --red:#ec1f27;
    --paper:#ffffff;
    --ink:#1d1d1f;
    --muted:#4a4a4a;
    --backdrop:#7d7d7f;
    --photo-light:#eef0f3;
    --photo-mid:#b7bfcc;
  }
  *{box-sizing:border-box;margin:0;padding:0}
  html,body{width:1200px;height:960px;overflow:hidden}
  body{background:var(--backdrop);position:relative;font-family:"Roboto Slab",Georgia,serif;color:var(--muted)}

  .sheet{position:absolute;background:var(--paper);box-shadow:0 6px 18px rgba(0,0,0,.25)}
  .brand-name{font-family:"Montserrat",Arial,sans-serif;font-weight:600;color:var(--ink);letter-spacing:.06em;line-height:1}

  .contact-list{list-style:none}
  .contact-list li{display:flex;align-items:center;gap:6px;line-height:1.35}
  .contact-list svg{flex:none}

  .address{line-height:1.3}
  .address .company{color:var(--red);display:flex;align-items:center;gap:6px}

  /* Letterhead */
  .letterhead{left:60px;top:40px;width:440px;height:622px;overflow:hidden}
  .letterhead .photo{position:absolute;inset:0 0 150px 0;
    background:linear-gradient(100deg,var(--photo-light) 0%,#f7f8fa 30%,var(--photo-mid) 55%,#d9dde4 75%,var(--photo-light) 100%);opacity:.75}
  .letterhead .photo-fade{position:absolute;left:0;right:0;top:330px;height:142px;background:linear-gradient(transparent,var(--paper))}
  .letterhead .footer{position:absolute;left:34px;right:30px;bottom:40px;display:flex;justify-content:space-between;align-items:flex-end}
  .letterhead .brand-name{font-size:22px}
  .letterhead .contact-list,.letterhead .address{font-size:10px}

  /* Business cards */
  .card{width:300px;height:172px;left:580px}
  .card-front{top:60px;display:flex;flex-direction:column;align-items:center;justify-content:center;gap:26px}
  .card-front .brand-name{font-size:26px}
  .card-front .web{font-size:10px;color:var(--muted)}
  .card-front .web span{color:var(--red)}
  .card-back{top:258px;overflow:hidden;padding:22px 22px 0 120px}
  .card-back .accent{position:absolute;left:0;top:0}
  .card-back .contact-list,.card-back .address{font-size:10px}
  .card-back .address{margin-top:12px}

  /* Envelope */
  .envelope{left:380px;top:520px;width:760px;height:380px;padding:40px 48px}
  .envelope .contact-list{font-size:15px}
  .envelope .contact-list svg{width:12px;height:12px}
  .envelope .sender{position:absolute;right:60px;bottom:56px;width:260px}
  .envelope .brand-name{font-size:36px;margin-bottom:34px}
  .envelope .address{font-size:16px}
</style>
</head>
<body>

<svg width="0" height="0" style="position:absolute">
  <defs>
    <symbol id="icon-dot" viewBox="0 0 10 10"><circle cx="5" cy="5" r="5" fill="#ec1f27"/><circle cx="5" cy="5" r="1.8" fill="#fff"/></symbol>
  </defs>
</svg>

<!-- Letterhead -->
<section class="sheet letterhead">
  <div class="photo" role="img" aria-label="Faded photograph of a gentleman in a pinstripe double-breasted suit beside bright windows"></div>
  <div class="photo-fade"></div>
  <div class="footer">
    <div>
      <p class="brand-name">VELMARDO</p>
    </div>
    <ul class="contact-list">
      <li><svg width="9" height="9"><use href="#icon-dot"/></svg>info@velmardo.com</li>
      <li><svg width="9" height="9"><use href="#icon-dot"/></svg>www.velmardo.ch</li>
      <li><svg width="9" height="9"><use href="#icon-dot"/></svg>+41 61 508 37 14</li>
      <li><svg width="9" height="9"><use href="#icon-dot"/></svg>+41 79 842 07 91</li>
    </ul>
    <div class="address">
      <p class="company"><svg width="9" height="9"><use href="#icon-dot"/></svg>VELMARDO AG</p>
      <p>Sonnwiesweg 27</p>
      <p>4068 Basel</p>
      <p>Switzerland</p>
    </div>
  </div>
</section>

<!-- Business card front -->
<section class="sheet card card-front">
  <p class="brand-name">VELMARDO</p>
  <p class="web">www.<span>velmardo</span>.ch</p>
</section>

<!-- Business card back -->
<section class="sheet card card-back">
  <svg class="accent" width="100" height="172" viewBox="0 0 100 172" aria-hidden="true">
    <polygon points="96,0 100,0 8,172 0,172" fill="#ec1f27"/>
  </svg>
  <ul class="contact-list">
    <li><svg width="9" height="9"><use href="#icon-dot"/></svg>info@velmardo.com</li>
    <li><svg width="9" height="9"><use href="#icon-dot"/></svg>www.velmardo.ch</li>
    <li><svg width="9" height="9"><use href="#icon-dot"/></svg>+41 61 508 37 14</li>
    <li><svg width="9" height="9"><use href="#icon-dot"/></svg>+41 79 842 07 91</li>
  </ul>
  <div class="address">
    <p class="company"><svg width="9" height="9"><use href="#icon-dot"/></svg>VELMARDO AG</p>
    <p>Sonnwiesweg 27</p>
    <p>4068 Basel</p>
    <p>Switzerland</p>
  </div>
</section>

<!-- Envelope -->
<section class="sheet envelope">
  <ul class="contact-list">
    <li><svg><use href="#icon-dot"/></svg>info@velmardo.com</li>
    <li><svg><use href="#icon-dot"/></svg>www.velmardo.ch</li>
    <li><svg><use href="#icon-dot"/></svg>+41 61 508 37 14</li>
    <li><svg><use href="#icon-dot"/></svg>+41 79 842 07 91</li>
  </ul>
  <div class="sender">
    <p class="brand-name">VELMARDO</p>
    <div class="address">
      <p class="company"><svg width="12" height="12"><use href="#icon-dot"/></svg>VELMARDO AG</p>
      <p>Sonnwiesweg 27</p>
      <p>4068 Basel</p>
      <p>Switzerland</p>
    </div>
  </div>
</section>

</body>
</html>
```